Bref créative
Newspaper Ad for Immigration Law Firm
Need Three Ads/Sizes
I need a total of 3 newspaper ads with 3 different sizes.
1. Main Ad - 5 in x 2 in
2. 3.25 in x 2 in
3. 1.5 in x 2 in
Designers should submit their design based on the 5 in x 2 in. Once I have determined the "winning designer," I will work with that designer to create the other two ads using the same winning design.
Law
The following must be included: I will also upload my picture, my logo, and Board Certified Logo. Thanks.
1. Picture of Attorney
2. Attorney
3. Brian K. Wendell
4. Law Firm logo
5. Board Certified Logo
6. Immigration Law below Board Certified Logo
7. 4180 Millbrook Lane
8. Suite 318
9. Houston, Texas 77043
10. www.thewendellcounsel.com
11. Telephone: (713) 548-2190
12. Fax: (713) 548-2197
13. bkellan4471@mailvexo.com
14. Immigration Bonds
15. Deportation Cases
16. Immigration Court
17. Immigration Waivers
18. Immigration Appeals
19. Family Petitions
20. Citizenship
21. Permanent Residency
22. Asylum, TPS, NACARA
23. Work Permits
24. Other Immigration Cases
Law Firm Logo Should go on the very top i think
You can cut out background if you like. Or not, up to your design.
The phrase "Immigration Law" must be directly underneath this logo. Logo cannot be changed or altered.
Sample proof

```html
<!DOCTYPE html>
<html lang="en">
<head>
<meta charset="utf-8">
<title>Brian K. Wendell Immigration Law Firm – Newspaper Ad</title>
<link rel="stylesheet" href="https://fonts.googleapis.com/css2?family=Cinzel:wght@400;700&family=Oswald:wght@400;500&family=Tinos:wght@400&display=swap">
<style>
  :root {
    --backdrop: #e9e9e9;
    --paper: #ffffff;
    --maroon: #5a1414;
    --band-dark: #2a0a0a;
    --band-mid: #6a1a18;
    --ink: #1d1d1d;
    --muted: #3a3a3a;
    --light: #ffffff;
    --badge: #1f3f73;
    --photo-a: #6b3b25;
    --photo-b: #2b150d;
  }
  * { box-sizing: border-box; margin: 0; padding: 0; }
  html, body { width: 1200px; height: 901px; overflow: hidden; }
  body { background: var(--backdrop); position: relative; }

  .ad {
    position: absolute; left: 80px; top: 130px;
    width: 1040px; height: 640px;
    background: var(--paper);
    overflow: hidden;
    box-shadow: 0 2px 10px rgba(0,0,0,.18);
  }

  .ad-header {
    position: absolute; left: 0; top: 0; width: 790px; height: 175px;
    background: linear-gradient(180deg, #ffffff 0%, #f1f1f1 100%);
  }
  .firm-mark {
    position: absolute; left: 40px; top: 40px; width: 80px; height: 96px;
    background: var(--maroon);
  }
  .firm-name {
    position: absolute; left: 140px; top: 26px; width: 440px;
    text-align: center; color: var(--maroon);
    font-family: "Cinzel", serif; font-weight: 400; line-height: 1.1;
  }
  .firm-name .line-small { display: block; font-size: 28px; }
  .firm-name .line-large { display: block; font-size: 54px; }
  .firm-name .line-mid { display: block; font-size: 28px; letter-spacing: 1px; }

  .certification {
    position: absolute; left: 600px; top: 28px; width: 180px;
  }
  .certification-badge {
    width: 180px; height: 64px; background: var(--badge); border-radius: 4px;
  }
  .certification-label {
    margin-top: 8px; font-family: "Tinos", serif; font-size: 18px;
    color: var(--muted); text-align: center;
  }

  .attorney-photo {
    position: absolute; right: 0; top: 0; width: 250px; height: 533px;
    background: radial-gradient(ellipse at 55% 35%, var(--photo-a) 0%, var(--photo-b) 80%);
  }
  .attorney-caption {
    position: absolute; right: 20px; top: 450px; width: 210px;
    text-align: center; color: var(--light);
    font-family: "Cinzel", serif; line-height: 1.2;
  }
  .attorney-caption .name { display: block; font-size: 20px; }
  .attorney-caption .title { display: block; font-size: 15px; letter-spacing: 1px; }

  .practice-band {
    position: absolute; left: 0; top: 175px; width: 790px; height: 358px;
    background: linear-gradient(90deg, var(--band-dark) 0%, var(--band-mid) 100%);
    display: flex; gap: 30px; padding: 28px 0 0 44px;
  }
  .practice-list { list-style: none; color: var(--light);
    font-family: "Oswald", sans-serif; font-weight: 400; font-size: 33px; line-height: 48px; }
  .practice-list li { position: relative; padding-left: 24px; }
  .practice-list li::before {
    content: ""; position: absolute; left: 0; top: 21px;
    width: 8px; height: 8px; border-radius: 50%; background: var(--light);
  }
  .practice-list.primary { width: 400px; }
  .practice-list li.wrap { line-height: 38px; padding-top: 5px; }

  .contact-strip {
    position: absolute; left: 0; top: 533px; width: 1040px; height: 107px;
    background: var(--paper);
  }
  .contact-details {
    position: absolute; left: 30px; top: 14px;
    font-family: "Tinos", serif; font-size: 19px; line-height: 25px; color: var(--ink);
  }
  .contact-details .web { letter-spacing: 4px; font-size: 21px; }
  .contact-details .gap { display: inline-block; width: 40px; }
  .phone-box {
    position: absolute; right: 0; top: 0; width: 390px; height: 80px;
    background: var(--band-dark);
    display: flex; align-items: center; justify-content: center;
    font-family: "Tinos", serif; font-size: 54px; color: var(--light);
  }
</style>
</head>
<body>
  <section class="ad">
    <header class="ad-header">
      <div class="firm-mark"></div>
      <div class="firm-name">
        <span class="line-small">Law Office of</span>
        <span class="line-large">Brian K. Wendell</span>
        <span class="line-mid">Immigration Law Firm</span>
      </div>
      <div class="certification">
        <div class="certification-badge"></div>
        <p class="certification-label">Immigration Law</p>
      </div>
    </header>

    <div class="attorney-photo" role="img" aria-label="Portrait photo of attorney Brian K. Wendell in a dark suit"></div>
    <div class="attorney-caption">
      <span class="name">Brian K. Wendell</span>
      <span class="title">Attorney</span>
    </div>

    <div class="practice-band">
      <ul class="practice-list primary">
        <li>Immigration Bonds</li>
        <li>Deportation Cases</li>
        <li>Immigration Court</li>
        <li>Immigration Waivers</li>
        <li>Immigration Appeals</li>
        <li>Family Petitions</li>
      </ul>
      <ul class="practice-list secondary">
        <li>Citizenship</li>
        <li>Permanent Residency</li>
        <li>Asylum, TPS, NACARA</li>
        <li>Work Permits</li>
        <li class="wrap">Other Immigration<br>Cases</li>
      </ul>
    </div>

    <footer class="contact-strip">
      <div class="contact-details">
        <p>4180 Millbrook Lane Suite 318 Houston, Texas 77043</p>
        <p>Fax: (713) 548-2197<span class="gap"></span>Email: bkellan4471@mailvexo.com</p>
        <p class="web">www.thewendellcounsel.com</p>
      </div>
      <div class="phone-box">(713) 548-2190</div>
    </footer>
  </section>
</body>
</html>
```